Corvane Holdings , new business card design

investment firm with corporate clients . need double sided business card , vertical and horizontal options ,logo must be clear. prefer pantone colors only and sharp design. website also www.corvane-example.ae

Khalid Bin Rashed
Managing Director
Tel. +971 4 000 3829
Mobile +971 50 000 4172
khalid@corvane-example.ae
Palm Crest Tower, officw 18-B07, Qasr Gardens, Dubai

Contact Information for Business Card

Khalid Bin Rashed
Managing Director

Font styles to use
Serif

Colors

Designer to choose colors to be used in the design.

```html
<!DOCTYPE html>
<html lang="en">
<head>
<meta charset="utf-8">
<title>Corvane Holdings – Business Card</title>
<link href="https://fonts.googleapis.com/css2?family=Roboto:wght@300;400;700&display=swap" rel="stylesheet">
<style>
  :root {
    --stage: #e6e3df;
    --card-white: #f4f4f3;
    --brand-blue: #45739d;
    --ink: #2b2b2b;
    --ink-soft: #555555;
    --rule: #6a6a6a;
    --white: #ffffff;
  }
  * { margin: 0; padding: 0; box-sizing: border-box; }
  html, body {
    width: 1200px; height: 911px; overflow: hidden;
    background: var(--stage);
    font-family: "Roboto", Arial, sans-serif;
  }
  .canvas { position: relative; width: 1200px; height: 911px; }

  .card { position: absolute; box-shadow: 0 6px 18px rgba(0,0,0,0.18); }

  /* Front – vertical */
  .card-front {
    left: 90px; top: 158px; width: 340px; height: 595px;
    background: var(--card-white);
    display: flex; flex-direction: column; align-items: center;
    text-align: center; padding-top: 72px;
  }
  .brand-name {
    font-weight: 300; text-transform: uppercase;
    letter-spacing: 0.32em; line-height: 1.5;
  }
  .card-front .brand-name { color: var(--brand-blue); font-size: 19px; width: 240px; }
  .holder { margin-top: 86px; }
  .holder-name {
    color: var(--brand-blue); font-weight: 700; font-size: 17px;
    text-transform: uppercase; letter-spacing: -0.01em;
  }
  .holder-title {
    color: var(--ink); font-weight: 700; font-size: 13px;
    text-transform: uppercase; margin-top: 2px;
  }
  .contact-block { width: 240px; margin-top: 14px; }
  .divider {
    position: relative; height: 1px; background: var(--rule); width: 100%;
  }
  .divider::after {
    content: ""; position: absolute; left: 50%; top: 1px;
    width: 26px; height: 4px; margin-left: -13px; background: var(--brand-blue);
  }
  .contact-group {
    padding: 12px 0 10px; color: var(--ink-soft);
    font-size: 13px; line-height: 1.5;
  }
  .spaced { letter-spacing: 0.35em; }

  /* Back – horizontal */
  .card-back {
    left: 500px; top: 285px; width: 620px; height: 354px;
    background: var(--brand-blue);
  }
  .card-back .brand-name {
    position: absolute; left: 0; right: 0; top: 150px;
    text-align: center; color: var(--white); font-size: 30px;
  }
  .back-web {
    position: absolute; left: 0; right: 0; top: 40px;
    text-align: center; color: var(--white); opacity: 0.85;
    font-size: 12px; font-weight: 300; letter-spacing: 0.8em;
  }
</style>
</head>
<body>
<main class="canvas">

  <section class="card card-front" aria-label="Business card front">
    <div class="brand-name">Corvane Holdings</div>

    <div class="holder">
      <p class="holder-name">Khalid Bin Rashed</p>
      <p class="holder-title">Managing Director</p>
    </div>

    <div class="contact-block">
      <div class="divider"></div>
      <div class="contact-group">
        <p>+971 4 000 3829</p>
        <p>+971 50 000 4172</p>
      </div>
      <div class="divider"></div>
      <div class="contact-group">
        <p>khalid@corvane-example.ae</p>
        <p class="spaced">www.corvane-example.ae</p>
      </div>
      <div class="divider"></div>
      <div class="contact-group">
        <p>Palm Crest Tower, officw 18-B07</p>
        <p>Qasr Gardens, Dubai</p>
      </div>
      <div class="divider"></div>
    </div>
  </section>

  <section class="card card-back" aria-label="Business card back">
    <p class="back-web">www.corvane-example.ae</p>
    <div class="brand-name">Corvane Holdings</div>
  </section>

</main>
</body>
</html>
```